Redesign for Real Estate Lead Generation Site

We are looking for a slight redesign for our real estate lead generation sites.

Here's one of our current sites: www.qdrhousefigures.com

The design should be simple as it is currently, remain only on one page, and nothing too detailed to where it may take a while to load/reload. We also have parallel sites, www.lmnhousefigures.com, www.lmnquicklistings.com, and a few others which all will end up utilizing the same template.

We've found that the majority of the site traffic will come from print advertising, not as much SEO. But also understand the more simple the site, the greater likelihood a user may find us through search engines. Another reason we want to keep it rather simple and clean.

The content on the page needs to remain the same, but with additional spaces for one written paragraph testimonial, and an area where we can incorporate a video. Originally, the ideal spot would be the open white space below the social media logos, but we are open to different ideas as you create the redesign.

A change in colors and simple graphics is what we're looking for most along with the testimonial / video additions. Also, we have a new logo we need incorporated into the site somewhere: http://www.brennoprintworks.com/KV-Crew-Properties.zip to download the file in different formates.

Here is our main site, www.kvcrewproperties.com through wordpress, so you can get an idea of what folks go to once they've signed up and received a confirm e-mail.

Please contact us if you have any questions. Good luck and thanks for submitting!

```html
<!DOCTYPE html>
<html lang="en">
<head>
<meta charset="utf-8">
<title>Fairfax VA Home Values – KV Crew Properties</title>
<link href="https://fonts.googleapis.com/css2?family=Arimo:wght@400;700&display=swap" rel="stylesheet">
<style>
  :root {
    --amber: #fbb516;
    --amber-deep: #f29f05;
    --ink: #262626;
    --label: #3a3a3a;
    --panel: #efefef;
    --bubble: #d4d4d4;
    --footer: #a3a3a3;
    --field-border: #c9d3e0;
    --field-glow: #e6edf6;
    --black: #000;
    --white: #fff;
    --sky-top: #3b7bc4;
    --sky-low: #a9cbe9;
    --video-fill: #8a9a8e;
    --control-bar: #e9e9e9;
  }
  * { box-sizing: border-box; margin: 0; padding: 0; }
  html, body { width: 1173px; height: 1200px; overflow: hidden; }
  body { position: relative; background: var(--white); font-family: "Arimo", Arial, sans-serif; color: var(--ink); }

  .hero { position: absolute; left: 111px; top: 0; width: 958px; height: 200px;
    background: linear-gradient(180deg, var(--sky-top) 0%, #6fa3d8 55%, var(--sky-low) 100%); }
  .hero-band { position: absolute; left: 111px; top: 200px; width: 958px; height: 83px; background: var(--black); }
  .brand { position: absolute; left: 141px; top: 0; width: 126px; height: 87px; background: var(--white);
    display: flex; align-items: center; justify-content: center; text-align: center;
    font-weight: 700; font-size: 14px; line-height: 16px; color: var(--ink); padding: 0 10px; }
  .hero-title { position: absolute; left: 146px; top: 136px; font-size: 37px; font-weight: 700; color: var(--white); letter-spacing: -0.3px; }

  .intro { position: absolute; left: 133px; top: 221px; width: 917px; height: 112px;
    background: linear-gradient(180deg, #fafafa 0%, #e3e3e3 100%); padding: 21px 50px 0 39px;
    font-size: 16.5px; font-weight: 700; line-height: 21px; color: var(--label); }

  .section-bar { position: absolute; left: 130px; width: 456px; height: 34px; background: var(--amber);
    border-radius: 4px 4px 0 0; font-size: 17px; font-weight: 700; color: var(--ink); padding: 7px 18px; }
  .field-label { position: absolute; font-size: 13px; font-weight: 700; color: var(--label); }
  .field { position: absolute; background: var(--white); border: 2px solid var(--field-border);
    box-shadow: inset 0 0 0 2px var(--field-glow); border-radius: 2px; }
  .select { font-size: 13px; color: var(--label); padding: 9px 13px; }
  .select svg { position: absolute; right: 12px; top: 15px; }
  .sign-up { position: absolute; left: 433px; top: 1042px; width: 156px; height: 40px;
    background: linear-gradient(180deg, var(--amber) 0%, var(--amber-deep) 100%); color: var(--white);
    font-size: 20px; font-weight: 700; text-align: center; line-height: 40px; border-radius: 3px; }

  .video-panel { position: absolute; left: 614px; top: 373px; width: 436px; height: 350px; background: var(--panel); border-radius: 4px; }
  .panel-title { position: absolute; left: 22px; top: 24px; font-size: 17px; font-weight: 700; color: var(--ink); }
  .video-frame { position: absolute; left: 17px; top: 46px; width: 404px; height: 251px; background: var(--video-fill); }
  .play { position: absolute; left: 177px; top: 86px; }
  .controls { position: absolute; left: 17px; top: 297px; width: 404px; height: 27px; }
  .time { position: absolute; left: 259px; top: 302px; font-size: 8px; color: #666; }

  .testimonial { position: absolute; left: 615px; top: 737px; width: 435px; height: 208px; background: var(--bubble); border-radius: 3px;
    padding: 26px 22px 0 22px; font-size: 13.6px; line-height: 19.5px; color: var(--ink); }
  .testimonial-author { position: absolute; right: 32px; top: 157px; font-weight: 700; font-size: 13px; font-style: normal; }
  .bubble-tail { position: absolute; left: 955px; top: 944px; }

  .social { position: absolute; left: 614px; top: 1002px; width: 436px; height: 80px; background: var(--panel); border-radius: 3px; }
  .social-title { position: absolute; left: 25px; top: 28px; font-size: 22px; font-weight: 700; color: var(--label); }
  .social-link { position: absolute; top: 20px; width: 37px; height: 38px; border-radius: 5px; }
  .social-link.one { left: 285px; background: #3b5998; }
  .social-link.two { left: 334px; background: #cfcfcf; }
  .social-link.three { left: 385px; background: #8fcbe3; }

  .footer { position: absolute; left: 133px; top: 1112px; width: 917px; height: 49px; background: var(--footer); border-radius: 10px;
    color: var(--white); font-size: 13px; font-weight: 700; display: flex; justify-content: space-between; align-items: center; padding: 0 20px 0 24px; }
</style>
</head>
<body>
  <header>
    <div class="hero" role="img" aria-label="Blue sky with clouds above a two-storey family home with a wraparound porch"></div>
    <div class="hero-band"></div>
    <div class="brand">KV Crew Properties</div>
    <h1 class="hero-title">Fairfax VA Home Values</h1>
  </header>

  <p class="intro">Fill out the form below for a FREE Comparative Market Analysis Report from KV Crew Properties for an estimate of your home's current value. The more complete the form the easier it will be to provide an accurate report regarding the value of your home.</p>

  <form class="lead-form">
    <div class="section-bar" style="top:373px">Personal Information</div>
    <span class="field-label" style="left:132px;top:418px">Name</span>
    <div class="field" style="left:132px;top:443px;width:454px;height:35px"></div>
    <span class="field-label" style="left:132px;top:491px">Email</span>
    <span class="field-label" style="left:373px;top:494px">Phone</span>
    <div class="field" style="left:132px;top:515px;width:216px;height:35px"></div>
    <div class="field" style="left:371px;top:515px;width:215px;height:35px"></div>

    <div class="section-bar" style="top:568px">Property Address</div>
    <span class="field-label" style="left:132px;top:616px">Street Address</span>
    <div class="field" style="left:132px;top:641px;width:454px;height:35px"></div>
    <span class="field-label" style="left:132px;top:691px">City</span>
    <span class="field-label" style="left:289px;top:691px">State</span>
    <span class="field-label" style="left:452px;top:691px">Zip</span>
    <div class="field" style="left:132px;top:716px;width:134px;height:36px"></div>
    <div class="field select" style="left:289px;top:716px;width:136px;height:36px">VA
      <svg width="10" height="6" viewBox="0 0 10 6"><path d="M0 0h10L5 6z" fill="#5a7fb5"/></svg></div>
    <div class="field" style="left:452px;top:716px;width:133px;height:36px"></div>

    <div class="section-bar" style="top:776px">Property Description</div>
    <span class="field-label" style="left:132px;top:826px">Number of bedroom</span>
    <span class="field-label" style="left:292px;top:826px">Number of Bathrooms</span>
    <span class="field-label" style="left:452px;top:828px">Condition</span>
    <div class="field select" style="left:132px;top:851px;width:133px;height:36px">Any
      <svg width="10" height="6" viewBox="0 0 10 6"><path d="M0 0h10L5 6z" fill="#5a7fb5"/></svg></div>
    <div class="field select" style="left:292px;top:851px;width:133px;height:36px">Any
      <svg width="10" height="6" viewBox="0 0 10 6"><path d="M0 0h10L5 6z" fill="#5a7fb5"/></svg></div>
    <div class="field select" style="left:452px;top:851px;width:131px;height:36px">Any
      <svg width="10" height="6" viewBox="0 0 10 6"><path d="M0 0h10L5 6z" fill="#5a7fb5"/></svg></div>
    <span class="field-label" style="left:133px;top:905px">Additional Comments</span>
    <div class="field" style="left:132px;top:929px;width:454px;height:96px"></div>
    <div class="sign-up">SIGN UP</div>
  </form>

  <section class="video-panel">
    <h2 class="panel-title">Video Feature</h2>
    <div class="video-frame" role="img" aria-label="Video still of a two-storey home on a green lawn">
      <svg class="play" width="70" height="70" viewBox="0 0 70 70">
        <circle cx="35" cy="35" r="34" fill="#d9d9d9" opacity="0.85"/>
        <circle cx="35" cy="35" r="27" fill="#f4a100"/>
        <path d="M28 22 L49 35 L28 48 Z" fill="#fff"/>
      </svg>
    </div>
    <svg class="controls" width="404" height="27" viewBox="0 0 404 27">
      <rect width="404" height="27" fill="var(--control-bar)"/>
      <path d="M8 9 L15 13.5 L8 18 Z" fill="#555"/>
      <rect x="35" y="11" width="200" height="5" rx="2.5" fill="#777"/>
      <rect x="35" y="11" width="99" height="5" rx="2.5" fill="#f4a100"/>
      <circle cx="134" cy="13.5" r="4" fill="#eee" stroke="#888"/>
      <path d="M300 11h3l4-3v11l-4-3h-3z" fill="#555"/>
      <rect x="316" y="11" width="50" height="5" rx="2.5" fill="#666"/>
      <circle cx="362" cy="13.5" r="3.5" fill="#eee" stroke="#888"/>
      <rect x="385" y="9" width="8" height="8" fill="none" stroke="#555" stroke-width="1.5"/>
    </svg>
    <span class="time">3:47 / 9:29</span>
  </section>

  <blockquote class="testimonial">
    ed ut perspiciatis unde omnis iste natus error sit volupta-tem accusantium doloremque laudantium, totam rem aperiam, eaque ipsa quae ab illo inventore veritatis et quasi architecto beatae vitae dicta sunt explicabo. Nemo enim ipsam voluptatem quia voluptas sit aspernatur aut odit aut fugit, sed quia consequuntur magni dolores eos qui ratione
    <cite class="testimonial-author">Maren Holloway, July 2011</cite>
  </blockquote>
  <svg class="bubble-tail" width="28" height="30" viewBox="0 0 28 30"><path d="M0 0H28L0 30Z" fill="var(--bubble)"/></svg>

  <section class="social">
    <h2 class="social-title">Join Our Conversation:</h2>
    <span class="social-link one" aria-label="Social link one"></span>
    <span class="social-link two" aria-label="Social link two"></span>
    <span class="social-link three" aria-label="Social link three"></span>
  </section>

  <footer class="footer">
    <span>© 2010 KV Crew Properties</span>
    <span>KV Crew Properties :: Summit 30 New Horizon :: 855-VA-LISTS :: info@kvcrewproperties.com</span>
  </footer>
</body>
</html>
```